LOGO DESIGN: Construction Related Service Business

We require a logo for our business Tovar Services. We are a construction related business offering a range of services including machine services for groundworks (digging trenches, soak wells, preparing land for construction etc), demolition and truck haulage from demolition sites.
We would like our logo to be predominately text, but may include abstract graphics. The colour scheme should be mainly a mid bright blue and overall be quite 'clean'.

Industry/Entity Type

Construction

Contact Information for Business Card

Dale Morrow
Ph:041 592 3068
tovarservices@quillnet.com.au

Colors
0456a3

```html
<!DOCTYPE html>
<html lang="en">
<head>
<meta charset="utf-8">
<title>Tovar Services – Business Card</title>
<link rel="stylesheet" href="https://fonts.googleapis.com/css2?family=Arimo:wght@700&family=Tinos:wght@700&family=Gelasio:ital@1&display=swap">
<style>
  :root {
    --page: #ffffff;
    --card: #f8f6f8;
    --brand-blue: #0b55a0;
    --ink-navy: #0f4a6e;
    --ink-dark: #0e3550;
    --band: #00446b;
  }
  html, body {
    margin: 0;
    padding: 0;
    overflow: hidden;
    background: var(--page);
  }
  .card-canvas {
    position: relative;
    width: 1200px;
    height: 686px;
    background: var(--page);
    overflow: hidden;
  }
  .card {
    position: absolute;
    left: 9px;
    top: 6px;
    width: 1180px;
    height: 665px;
    background: var(--card);
  }
  .brand-mark {
    position: absolute;
    left: 466px;
    top: 54px;
    width: 250px;
    height: 250px;
    border-radius: 50%;
    background: var(--brand-blue);
  }
  .brand-name {
    position: absolute;
    left: 0;
    width: 100%;
    top: 326px;
    margin: 0;
    text-align: center;
    font-family: "Arimo", Arial, sans-serif;
    font-weight: 700;
    font-size: 58px;
    letter-spacing: 2px;
    color: var(--brand-blue);
    line-height: 1;
  }
  .contact-name {
    position: absolute;
    left: 24px;
    top: 523px;
    margin: 0;
    font-family: "Tinos", "Times New Roman", serif;
    font-weight: 700;
    font-size: 46px;
    color: var(--ink-navy);
    line-height: 1;
  }
  .contact-line {
    position: absolute;
    left: 580px;
    display: flex;
    align-items: center;
    font-family: "Gelasio", Georgia, serif;
    font-style: italic;
    font-size: 31px;
    color: var(--ink-dark);
    line-height: 1;
    white-space: nowrap;
  }
  .contact-phone { top: 528px; }
  .contact-email { top: 593px; }
  .contact-icon {
    flex: none;
    fill: var(--ink-dark);
    margin-right: 18px;
  }
  .contact-band {
    position: absolute;
    left: 9px;
    top: 642px;
    width: 1180px;
    height: 29px;
    background: var(--band);
  }
</style>
</head>
<body>
  <div class="card-canvas">
    <section class="card">
      <div class="brand-mark" aria-hidden="true"></div>
      <h1 class="brand-name">Tovar Services</h1>

      <p class="contact-name">Dale Morrow</p>

      <div class="contact-line contact-phone">
        <svg class="contact-icon" width="58" height="42" viewBox="0 0 58 42" aria-hidden="true">
          <path d="M2 12 C2 3 12 1 29 1 C46 1 56 3 56 12 L56 16 L44 16 L44 10 L14 10 L14 16 L2 16 Z"/>
          <path d="M18 13 L40 13 L48 30 L48 41 L10 41 L10 30 Z"/>
          <circle cx="29" cy="28" r="8" fill="var(--card)"/>
          <circle cx="29" cy="28" r="3.5"/>
        </svg>
        <span>+ 041 592 3068</span>
      </div>

      <div class="contact-line contact-email">
        <svg class="contact-icon" width="54" height="30" viewBox="0 0 54 30" aria-hidden="true">
          <rect x="1" y="1" width="52" height="28" fill="var(--ink-dark)"/>
          <path d="M4 3 L27 18 L50 3" fill="none" stroke="var(--card)" stroke-width="2.2"/>
          <path d="M4 27 L20 14 M50 27 L34 14" fill="none" stroke="var(--card)" stroke-width="2.2"/>
        </svg>
        <span>: tovarservices@quillnet.com.au</span>
      </div>
    </section>
    <div class="contact-band"></div>
  </div>
</body>
</html>
```